We need a business card design for an assisted living facility in Los Angeles. We have a logo selected but we would like a business card design that will leave a lasting impression on families looking to place their elderly loved ones in our care as well as on other facility providers who may refer their elderly residents to our facility.

```html
<!DOCTYPE html>
<html lang="en">
<head>
<meta charset="utf-8">
<title>Kingsbridge Manor Senior Living – Business Card</title>
<link rel="stylesheet" href="https://fonts.googleapis.com/css2?family=Crimson+Text:wght@400;600&display=swap">
<style>
  :root {
    --bg: #2b2d30;
    --card-white: #ffffff;
    --card-grey: #828383;
    --brand-blue: #1268be;
    --edge-grey: #8c8c8c;
    --text-grey: #6f6f6f;
    --rule-grey: #cfcfcf;
  }
  * { margin: 0; padding: 0; box-sizing: border-box; }
  html, body { width: 1200px; height: 952px; overflow: hidden; background: var(--bg); }
  .stage { position: relative; width: 1200px; height: 952px; }

  .card {
    position: absolute;
    width: 540px;
    height: 308px;
    box-shadow: 0 14px 30px rgba(0,0,0,.45);
    overflow: hidden;
  }
  .card-edge {
    position: absolute; left: 0; right: 0; bottom: 0; height: 7px;
    background: linear-gradient(90deg, var(--edge-grey) 0 46%, var(--brand-blue) 46% 100%);
  }

  /* Company name placeholder: plain text, one colour, one weight */
  .company-name {
    display: flex; align-items: center; gap: 10px;
    font-family: "Crimson Text", serif; font-weight: 400;
    font-size: 24px; line-height: 1.2; letter-spacing: 0;
  }
  .company-mark { width: 14px; height: 14px; flex: none; }

  /* Front */
  .card-front { left: 50px; top: 500px; background: var(--card-white); }
  .card-front .company-name { position: absolute; left: 36px; top: 36px; color: var(--brand-blue); }
  .card-front .company-mark { background: var(--brand-blue); }
  .person { position: absolute; left: 36px; top: 104px; }
  .person-name {
    font-family: "Crimson Text", serif; font-weight: 600; color: var(--brand-blue);
    font-size: 18px; line-height: 1.2; text-transform: uppercase;
  }
  .person-title {
    font-family: "Crimson Text", serif; color: var(--text-grey); font-size: 12.5px; line-height: 1.3;
  }
  .title-rule { position: absolute; left: 36px; top: 152px; width: 468px; height: 1px; background: var(--rule-grey); }
  .contact-list { position: absolute; left: 36px; top: 164px; list-style: none; }
  .contact-list li {
    display: flex; align-items: center; gap: 8px; height: 20px;
    font-family: "Crimson Text", serif; color: var(--text-grey); font-size: 12.5px;
  }
  .icon { width: 14px; height: 14px; background: var(--brand-blue); border-radius: 2px; display: flex; align-items: center; justify-content: center; }
  .icon svg { width: 10px; height: 10px; }
  .address {
    position: absolute; right: 36px; bottom: 30px; text-align: right; font-style: normal;
    font-family: "Crimson Text", serif; color: var(--text-grey); font-size: 13px; line-height: 1.35;
  }

  /* Back */
  .card-back { left: 610px; top: 160px; background: var(--card-grey); }
  .card-back .company-name {
    position: absolute; left: 0; right: 0; top: 134px; justify-content: center;
    color: var(--card-white); font-size: 28px;
  }
  .card-back .company-mark { background: var(--card-white); width: 16px; height: 16px; }
</style>
</head>
<body>
<main class="stage">

  <section class="card card-front" aria-label="Business card front">
    <p class="company-name"><span class="company-mark"></span>Kingsbridge Manor Senior Living</p>
    <div class="person">
      <p class="person-name">Daniel R. Whitmore</p>
      <p class="person-title">Managing Director</p>
    </div>
    <div class="title-rule"></div>
    <ul class="contact-list">
      <li><span class="icon"><svg viewBox="0 0 10 10"><path d="M2 1.2l1.6-.2.8 2-1 .8a5 5 0 0 0 2.8 2.8l.8-1 2 .8-.2 1.6C5 8.3 1.7 5 2 1.2z" fill="#fff"/></svg></span>+1 213 555 0147</li>
      <li><span class="icon"><svg viewBox="0 0 10 10"><rect x="1" y="2.2" width="8" height="5.6" fill="none" stroke="#fff" stroke-width="1"/><path d="M1 2.4l4 3 4-3" fill="none" stroke="#fff" stroke-width="1"/></svg></span>hello@kingsbridgemanor.com</li>
      <li><span class="icon"><svg viewBox="0 0 10 10"><path d="M2 2l6 2.6-2.5.9L4.6 8z" fill="#fff"/></svg></span>www.kingsbridgemanor.com</li>
    </ul>
    <address class="address">1520 Larkspur Avenue<br>Los Angeles<br>CA 90012</address>
    <div class="card-edge"></div>
  </section>

  <section class="card card-back" aria-label="Business card back">
    <p class="company-name"><span class="company-mark"></span>Kingsbridge Manor Senior Living</p>
    <div class="card-edge"></div>
  </section>

</main>
</body>
</html>
```